Holiday Party Flyer Template

We are a company offering downloadable flyer designs to customers. We are seeking to broaden our design categories and would like to start with the party invitation category and in specific a Holiday themed party. There will be one winner but we will be following up with all designers who we feel have submitted quality work to discuss potentially licensing your designs so this could lead to much more work even if you dont win the contest. Please consider the following requirements and instructions:

* Holiday Party Flyer Design (Winter theme suitable for any small to large holdiay party event)

* Text elements to include: Event title, event location, event time and date, room for 2 to 3 paragraphs of text such as for attire, directions etc. Room for a company logo - note that the design should still look good if there is NOT a company logo since this may or may not be used by our client. Placeholder text can be used at the designers discretion in all areas described above. For example, you can feel free to call it "Winter Holiday Party" or "Annual Company Holiday Bash", etc. Its up to you - be creative.

* Design for letter size paper (8.5" by 11" 300dpi vector based!)

* If you only submit a single design, make sure the design does not contain anything specific to a certain religion (ie, Santa Claus, mangers and wise men or anything like that)

* Some of our clients may want to use the flyer design for Christmas or Hanukah themed events, so if you submit multiple designs, please feel free to include elements relating to these themes such as Santa and so on.

```html
<!DOCTYPE html>
<html lang="en">
<head>
<meta charset="utf-8">
<title>Annual Company Holiday Bash</title>
<link rel="stylesheet" href="https://fonts.googleapis.com/css2?family=Almendra:wght@700&family=Arimo:wght@400;700&family=Ultra&display=swap">
<style>
  :root {
    --red-deep: #5e0a0c;
    --red-mid: #a3100f;
    --red-bright: #e5271c;
    --gold: #f6d98c;
    --gold-rgb: 233, 190, 100;
    --gold-dark: #b9862d;
    --ink: #0d0a0a;
    --white: #ffffff;
    --green: #7fcf2a;
    --green-dark: #2f7a10;
  }
  html, body { margin: 0; padding: 0; overflow: hidden; }
  body { width: 927px; height: 1200px; background: var(--ink); }
  .flyer {
    position: relative; width: 927px; height: 1200px; overflow: hidden;
    font-family: "Arimo", Arial, sans-serif;
    background: radial-gradient(ellipse 70% 55% at 68% 52%, var(--red-bright) 0%, var(--red-mid) 45%, var(--red-deep) 100%);
  }

  /* soft gold glows standing in for filigree corners */
  .corner { position: absolute; width: 84px; height: 84px; }
  .corner--tl { left: 30px; top: 36px;
    background: radial-gradient(circle at 0 0, rgba(var(--gold-rgb), .55) 0%, rgba(var(--gold-rgb), .18) 45%, rgba(var(--gold-rgb), 0) 72%); }
  .corner--tr { right: 30px; top: 36px;
    background: radial-gradient(circle at 100% 0, rgba(var(--gold-rgb), .55) 0%, rgba(var(--gold-rgb), .18) 45%, rgba(var(--gold-rgb), 0) 72%); }
  .corner--bl { left: 30px; top: 1080px;
    background: radial-gradient(circle at 0 100%, rgba(var(--gold-rgb), .5) 0%, rgba(var(--gold-rgb), .16) 45%, rgba(var(--gold-rgb), 0) 72%); }
  .corner--br { right: 30px; top: 1080px;
    background: radial-gradient(circle at 100% 100%, rgba(var(--gold-rgb), .5) 0%, rgba(var(--gold-rgb), .16) 45%, rgba(var(--gold-rgb), 0) 72%); }

  .when { position: absolute; top: 46px; width: 100%; text-align: center; color: var(--gold); }
  .when__date { font-weight: 700; font-size: 33px; line-height: 36px; }
  .when__time { font-size: 33px; line-height: 34px; }

  .divider { position: absolute; left: 286px; top: 133px; width: 355px; height: 3px;
    background: linear-gradient(90deg, rgba(var(--gold-rgb), .3), var(--gold-dark) 20%, var(--gold-dark) 80%, rgba(var(--gold-rgb), .3)); }
  .flourish {
    position: absolute; left: 366px; top: 137px; width: 195px; height: 80px;
    background: radial-gradient(ellipse 50% 50% at 50% 40%, rgba(var(--gold-rgb), .5) 0%, rgba(var(--gold-rgb), .2) 50%, rgba(var(--gold-rgb), 0) 100%);
  }

  .presenter {
    position: absolute; top: 227px; width: 100%; text-align: center;
    color: var(--gold); font-weight: 700; font-size: 21.5px; line-height: 26px;
  }

  .art {
    position: absolute; left: 65px; top: 284px; width: 797px; height: 534px;
    background: radial-gradient(ellipse 50% 48% at 50% 50%, rgba(240,200,110,.5) 0%, rgba(200,140,50,.3) 55%, rgba(163,16,15,0) 100%);
  }

  .title { margin: 0; font-weight: normal; }
  .title__line, .title__company {
    position: absolute; left: 0; width: 100%; text-align: center; white-space: nowrap;
  }
  .title__line {
    font-family: "Almendra", Georgia, serif; font-weight: 700; color: var(--white);
    text-shadow: 0 3px 0 #8a8a8a, 0 6px 10px rgba(0,0,0,.55);
  }
  .title__line--annual { top: 340px; font-size: 104px; line-height: 116px; }
  .title__line--bash { top: 583px; font-size: 100px; line-height: 120px; }
  .title__company {
    top: 452px; font-family: "Ultra", Georgia, serif;
    font-size: 120px; line-height: 120px; color: var(--green);
    text-shadow: 0 3px 0 var(--green-dark), 0 6px 10px rgba(0,0,0,.5);
  }

  .details { position: absolute; top: 838px; width: 100%; text-align: center; color: var(--gold); font-weight: 700; }
  .details__lead { font-size: 15px; line-height: 16px; letter-spacing: .6px; }
  .details__head { margin-top: 2px; font-size: 25px; line-height: 30px; letter-spacing: 1.5px; }
  .details__body { margin: 5px 0 0; font-size: 12px; line-height: 11.5px; }

  .footer {
    position: absolute; left: 0; top: 982px; width: 100%; height: 218px;
    background: linear-gradient(180deg, #141010 0%, var(--ink) 100%);
  }
  .sponsors { position: absolute; top: 1051px; left: 0; width: 100%; height: 24px; }
  .sponsor {
    position: absolute; transform: translateX(-50%); white-space: nowrap;
    color: var(--white); font-weight: 700; font-size: 17px; line-height: 24px;
    display: flex; align-items: center; gap: 6px;
  }
  .sponsor__dot { width: 14px; height: 14px; border-radius: 50%; background: var(--red-bright); }
  .contact {
    position: absolute; top: 1124px; width: 100%; text-align: center;
    color: var(--gold); font-size: 19.5px; line-height: 24px;
  }
  .contact strong { font-weight: 700; }
</style>
</head>
<body>
<div class="flyer">
  <div class="corner corner--tl" role="img" aria-label="Gold filigree corner ornament"></div>
  <div class="corner corner--tr" role="img" aria-label="Gold filigree corner ornament"></div>

  <div class="when">
    <div class="when__date">SUNDAY | 12.21.10</div>
    <div class="when__time">9:00AM-6:00</div>
  </div>
  <div class="divider"></div>
  <div class="flourish" role="img" aria-label="Gold scroll flourish below the rule"></div>
  <div class="presenter">LOREM IPSUM DOLOR SIT AMET PRESENTS</div>

  <div class="art" role="img" aria-label="Red gift bow, golden ribbons, round plaque and golden bells behind the title"></div>
  <h1 class="title">
    <span class="title__line title__line--annual">Annual</span>
    <span class="title__company">COMPANY</span>
    <span class="title__line title__line--bash">Holiday Bash</span>
  </h1>

  <div class="details">
    <div class="details__lead">LOREM IPSUM DOLOR SIT AMET<br>ARCU A JUSTO, DOLOR SEM</div>
    <div class="details__head">AENEAN FERMENTUM</div>
    <p class="details__body">LOREM IPSUM DOLOR SIT AMET, ARCU A JUSTO, DOLOR SEM AENEAN FERMENTUM<br>AT EU UT AMET SUSPENDISSE VESTIBULUM. UT FUSCE FAUCIBUS ALIQUAM PULVINAR INTEGER<br>AUGUE VESTIBULUM MAGNA AC IPSUM SCELERISQUE NIBH, EU UT DIGNISSIM AMET INTEGER<br>NULLAM LACUS, SEMPER MASSA LOBORTIS QUIS ET NUNC VITAE</p>
  </div>

  <div class="footer"></div>
  <div class="corner corner--bl" role="img" aria-label="Gold filigree corner ornament"></div>
  <div class="corner corner--br" role="img" aria-label="Gold filigree corner ornament"></div>

  <div class="sponsors">
    <div class="sponsor" style="left:196px"><span class="sponsor__dot"></span>Juniper</div>
    <div class="sponsor" style="left:343px">Loft Hall</div>
    <div class="sponsor" style="left:474px"><span class="sponsor__dot"></span>Turnabout</div>
    <div class="sponsor" style="left:605px">Brightwave</div>
    <div class="sponsor" style="left:739px">Solvia</div>
  </div>

  <div class="contact">LOREM IPSUM DOLOR SIT AMET <strong>0123456789</strong></div>
</div>
</body>
</html>
```